Financial firm simple design

Classic business card design for a financial fund. 2 sided card- white on both sides.. One with just the company name centered and the other w the info. info included on that is :

Name
Company position
phone number
fax
email
website

Financial

```html
<!DOCTYPE html>
<html lang="en">
<head>
<meta charset="UTF-8">
<title>Alder Investments — Business Card</title>
<link href="https://fonts.googleapis.com/css2?family=Cinzel:wght@400&family=PT+Sans:wght@400&display=swap" rel="stylesheet">
<style>
  :root {
    --backdrop: #e6e4e1;
    --card: #ffffff;
    --ink: #1c232c;
    --accent: #3f6f9e;
    --muted: #2e3640;
  }
  * { box-sizing: border-box; margin: 0; padding: 0; }
  html, body {
    width: 1200px;
    height: 800px;
    overflow: hidden;
    background: var(--backdrop);
  }
  .canvas {
    position: relative;
    width: 1200px;
    height: 800px;
    display: flex;
    align-items: center;
    justify-content: center;
    gap: 60px;
  }
  .card {
    width: 520px;
    height: 300px;
    background: var(--card);
    box-shadow: 0 6px 18px rgba(0,0,0,0.14), 0 1px 3px rgba(0,0,0,0.10);
    position: relative;
  }

  /* Contact side */
  .card--contact {
    display: flex;
    align-items: center;
  }
  .identity {
    width: 250px;
    padding-left: 70px;
  }
  .identity__name {
    font-family: 'Cinzel', serif;
    font-size: 22px;
    letter-spacing: 1px;
    color: var(--accent);
    line-height: 1.1;
  }
  .identity__role {
    font-family: 'PT Sans', sans-serif;
    font-size: 10px;
    letter-spacing: 0.5px;
    color: var(--muted);
    margin-top: 4px;
  }
  .divider {
    width: 1px;
    height: 96px;
    background: var(--accent);
    margin-right: 32px;
  }
  .contacts {
    list-style: none;
    font-family: 'PT Sans', sans-serif;
    font-size: 13px;
    color: var(--muted);
  }
  .contacts__item {
    display: flex;
    align-items: center;
    gap: 8px;
    line-height: 1;
    margin: 6px 0;
  }
  .contacts__icon {
    width: 12px;
    height: 12px;
    flex: none;
  }

  /* Brand side */
  .card--brand {
    display: flex;
    align-items: center;
    justify-content: center;
  }
  .brand__name {
    font-family: 'Cinzel', serif;
    font-weight: 400;
    font-size: 34px;
    letter-spacing: 2px;
    color: var(--ink);
  }
</style>
</head>
<body>
<main class="canvas">

  <section class="card card--contact" aria-label="Business card, contact side">
    <div class="identity">
      <p class="identity__name">Marcus Wen</p>
      <p class="identity__role">DIRECTOR</p>
    </div>
    <span class="divider"></span>
    <ul class="contacts">
      <li class="contacts__item">
        <svg class="contacts__icon" viewBox="0 0 12 12" aria-hidden="true">
          <rect width="12" height="12" rx="1.5" fill="#3f6f9e"/>
          <path d="M3.6 2.6 L5 4 L4.3 4.9 Q5.2 6.8 7.1 7.7 L8 7 L9.4 8.4 L8.5 9.4 Q4.8 9 2.6 3.5 Z" fill="#fff"/>
        </svg>
        <span>+852 5550 2841</span>
      </li>
      <li class="contacts__item">
        <svg class="contacts__icon" viewBox="0 0 12 12" aria-hidden="true">
          <rect width="12" height="12" rx="1.5" fill="#3f6f9e"/>
          <rect x="2.5" y="5" width="7" height="4.5" fill="#fff"/>
          <rect x="4" y="2.5" width="4" height="3" fill="#fff"/>
          <rect x="4" y="6.5" width="4" height="0.8" fill="#3f6f9e"/>
        </svg>
        <span>+852 5550 7319</span>
      </li>
      <li class="contacts__item">
        <svg class="contacts__icon" viewBox="0 0 12 12" aria-hidden="true">
          <rect width="12" height="12" rx="1.5" fill="#3f6f9e"/>
          <rect x="2.3" y="3.5" width="7.4" height="5" fill="#fff"/>
          <path d="M2.3 3.5 L6 6.4 L9.7 3.5" fill="none" stroke="#3f6f9e" stroke-width="0.8"/>
        </svg>
        <span>marcus.wen@alderinvest.com</span>
      </li>
      <li class="contacts__item">
        <svg class="contacts__icon" viewBox="0 0 12 12" aria-hidden="true">
          <rect width="12" height="12" rx="1.5" fill="#3f6f9e"/>
          <circle cx="6" cy="6" r="3.6" fill="none" stroke="#fff" stroke-width="0.8"/>
          <ellipse cx="6" cy="6" rx="1.5" ry="3.6" fill="none" stroke="#fff" stroke-width="0.7"/>
          <line x1="2.4" y1="6" x2="9.6" y2="6" stroke="#fff" stroke-width="0.7"/>
        </svg>
        <span>www.alderinvest.com</span>
      </li>
    </ul>
  </section>

  <section class="card card--brand" aria-label="Business card, brand side">
    <p class="brand__name">ALDER INVESTMENTS</p>
  </section>

</main>
</body>
</html>
```